Business Card Design Project

We need a Business Card for an Mechanical Engineering firm in Singapore. The design should be Modern & Technical looking, yet eye catching.

Our company deals in Cutting Tools & Machine Accessories for the Manufacturing Industries such as Oil & Gas, Aero Space, etc... For more information on our Company, you can either email me or view our website www.valtrion.com.sg.

We are trying to revamp our image to give our consumers a fresh new perspective to our company, so we welcome all ideas.

Industry/Entity Type

Business

Requirements
Must have
• Must incorporate New Company Logo into the card as shown in Uploaded file.

```html
<!DOCTYPE html>
<html lang="en">
<head>
<meta charset="utf-8">
<title>Valtrion Tools – Business Card</title>
<link rel="stylesheet" href="https://fonts.googleapis.com/css2?family=Yanone+Kaffeesatz:wght@300;400&display=swap">
<style>
  :root {
    --backdrop: #9c9c9c;
    --card-white: #ffffff;
    --brand-orange: #ff6600;
    --brand-black: #000000;
    --logo-grey: #5a5a5a;
    --rule-light: #ffb585;
    --title-dark: #2a2a2a;
  }
  html, body {
    margin: 0;
    width: 1200px;
    height: 879px;
    overflow: hidden;
    background: var(--backdrop);
    font-family: "Yanone Kaffeesatz", "Arial Narrow", sans-serif;
  }
  .stage { position: relative; width: 1200px; height: 879px; }
  .card {
    position: absolute;
    left: 336px;
    width: 424px;
    height: 242px;
    background: var(--card-white);
    overflow: hidden;
  }
  .card--back { top: 191px; }
  .card--front { top: 453px; }
  .card svg { position: absolute; inset: 0; display: block; }
  .card-text { font-family: "Yanone Kaffeesatz", "Arial Narrow", sans-serif; }
  .brand-name { font-weight: 400; font-size: 27px; letter-spacing: 0.5px; }
  .brand-name--light { fill: var(--card-white); }
  .brand-name--grey { fill: var(--logo-grey); }
  .holder-name { fill: var(--card-white); font-weight: 300; font-size: 34px; letter-spacing: 0.5px; }
  .holder-title { fill: var(--title-dark); font-weight: 400; font-size: 14px; }
</style>
</head>
<body>
<main class="stage">

  <svg width="0" height="0" style="position:absolute" aria-hidden="true">
    <defs>
      <linearGradient id="hole-fill" x1="0.2" y1="0.1" x2="0.8" y2="0.9">
        <stop offset="0" stop-color="#9a9a9a" stop-opacity="0.55"/>
        <stop offset="0.45" stop-color="#d8d8d8" stop-opacity="0.45"/>
        <stop offset="1" stop-color="#ffffff" stop-opacity="0.75"/>
      </linearGradient>
      <linearGradient id="hole-fill-solid" x1="0.2" y1="0.1" x2="0.8" y2="0.9">
        <stop offset="0" stop-color="#b5b5b5"/>
        <stop offset="0.5" stop-color="#e6e6e6"/>
        <stop offset="1" stop-color="#ffffff"/>
      </linearGradient>
      <filter id="hole-shadow" x="-50%" y="-50%" width="200%" height="200%">
        <feGaussianBlur stdDeviation="3"/>
      </filter>
    </defs>
  </svg>

  <section class="card card--back" aria-label="Card back">
    <svg viewBox="0 0 424 242" width="424" height="242">
      <path class="swoosh-orange" fill="var(--brand-orange)"
            d="M0,122 C140,72 300,22 424,12 L424,72 C404,128 376,186 362,242 L344,242 C352,176 340,118 300,104 C200,96 90,118 0,142 Z"/>
      <path class="field-black" fill="var(--brand-black)"
            d="M0,150 C90,126 200,104 288,106 C326,112 342,160 334,242 L0,242 Z"/>
      <g class="hole-grid">
        <g class="hole-shadows" fill="#000" opacity="0.45" filter="url(#hole-shadow)">
          <circle cx="211" cy="33" r="17"/><circle cx="273" cy="33" r="17"/><circle cx="334" cy="33" r="17"/><circle cx="395" cy="33" r="17"/>
          <circle cx="211" cy="76" r="17"/><circle cx="273" cy="76" r="17"/><circle cx="334" cy="76" r="17"/><circle cx="395" cy="76" r="17"/>
          <circle cx="211" cy="120" r="17"/><circle cx="273" cy="120" r="17"/><circle cx="334" cy="120" r="17"/><circle cx="395" cy="120" r="17"/>
        </g>
        <g class="hole-faces" fill="url(#hole-fill)">
          <circle cx="205" cy="27" r="17"/><circle cx="267" cy="27" r="17"/><circle cx="328" cy="27" r="17"/><circle cx="389" cy="27" r="17"/>
          <circle cx="205" cy="70" r="17"/><circle cx="267" cy="70" r="17"/><circle cx="328" cy="70" r="17"/><circle cx="389" cy="70" r="17"/>
          <circle cx="205" cy="114" r="17"/><circle cx="267" cy="114" r="17"/><circle cx="328" cy="114" r="17"/><circle cx="389" cy="114" r="17"/>
        </g>
      </g>
      <g class="brand-lockup">
        <circle cx="30" cy="206" r="9" fill="var(--card-white)"/>
        <text class="card-text brand-name brand-name--light" x="46" y="215">VALTRION TOOLS</text>
      </g>
    </svg>
  </section>

  <section class="card card--front" aria-label="Card front">
    <svg viewBox="0 0 424 242" width="424" height="242">
      <g class="holes-under">
        <circle cx="281" cy="34" r="28" fill="#000" opacity="0.45" filter="url(#hole-shadow)"/>
        <circle cx="274" cy="27" r="28" fill="url(#hole-fill-solid)"/>
        <circle cx="371" cy="44" r="30" fill="#000" opacity="0.45" filter="url(#hole-shadow)"/>
        <circle cx="364" cy="37" r="30" fill="url(#hole-fill-solid)"/>
      </g>
      <path class="swoosh-orange" fill="var(--brand-orange)"
            d="M0,18 C60,4 120,0 190,2 C290,8 380,44 424,92 L424,140 C300,112 160,128 100,242 L0,242 Z"/>
      <g class="holes-over">
        <circle cx="168" cy="190" r="32" fill="#000" opacity="0.45" filter="url(#hole-shadow)"/>
        <circle cx="161" cy="183" r="32" fill="url(#hole-fill-solid)"/>
      </g>
      <text class="card-text holder-name" x="22" y="64">Marcus Ellery</text>
      <text class="card-text holder-title" x="172" y="64">General Manager</text>
      <line class="name-rule" x1="20" y1="73" x2="256" y2="73" stroke="var(--rule-light)" stroke-width="0.8"/>
      <g class="brand-lockup">
        <circle cx="244" cy="204" r="9" fill="var(--logo-grey)"/>
        <text class="card-text brand-name brand-name--grey" x="260" y="213">VALTRION TOOLS</text>
      </g>
    </svg>
  </section>

</main>
</body>
</html>
```